TalkBridge - Language Coaching Services

Sleek, innovative, trendy design for Language Coaching business.

TalkBridge is a new UK based company that provides Language Coaching services. We offer highly personalized on-line and face to face language courses. We also impart learning techniques workshops based on the latest neuroscience research for second-language acquisition.

Target Market(s)

Industry/Entity Type

Consulting

Contact Information for Business Card

TalkBridge
ElenaVT@talkbridge-demo.co.uk
TalkBridge-demo.co.uk
London, UK

Font styles to use
Sans Serif

```html
<!DOCTYPE html>
<html lang="en">
<head>
<meta charset="utf-8">
<title>TalkBridge – Business Card</title>
<link href="https://fonts.googleapis.com/css2?family=Lato:wght@300;400;700;900&display=swap" rel="stylesheet">
<style>
  :root {
    --stage: #2e2f31;
    --paper: #f1f1f1;
    --blue: #0a8fd6;
    --blue-deep: #0b6fb3;
    --blue-light: #1eb0ea;
    --ink: #3d4146;
    --rule: #c9cccf;
    --white: #ffffff;
  }
  * { box-sizing: border-box; margin: 0; padding: 0; }
  html, body {
    width: 1200px; height: 896px; overflow: hidden;
    background: var(--stage);
    font-family: "Lato", sans-serif;
  }
  .stage {
    position: relative; width: 1200px; height: 896px;
    display: flex; flex-direction: column; align-items: center; justify-content: center; gap: 40px;
  }
  .card {
    position: relative; width: 700px; height: 400px; overflow: hidden;
    box-shadow: 0 10px 28px rgba(0,0,0,.45);
  }

  /* Front */
  .card--front { background: var(--paper); }
  .card--front .edge {
    position: absolute; left: 0; right: 0; bottom: 0; height: 12px;
    background: linear-gradient(90deg, var(--blue-light), var(--blue-deep));
  }
  .contact { position: absolute; left: 48px; top: 110px; width: 290px; }
  .contact .name {
    font-size: 28px; letter-spacing: 1px; color: var(--blue); text-transform: uppercase; line-height: 1;
    white-space: nowrap;
  }
  .contact .name .first { font-weight: 900; }
  .contact .name .last { font-weight: 300; }
  .contact .role { margin-top: 6px; font-size: 18px; color: var(--ink); font-weight: 400; }
  .contact .divider { margin: 12px 0 14px; height: 1px; background: var(--rule); width: 290px; }
  .contact ul { list-style: none; }
  .contact li {
    display: flex; align-items: center; gap: 10px;
    font-size: 16px; color: var(--ink); line-height: 1.55; white-space: nowrap;
  }
  .contact li svg { width: 15px; height: 15px; flex: none; }

  .brand {
    position: absolute; right: 48px; top: 70px;
    display: flex; flex-direction: column; align-items: flex-end; gap: 12px;
  }
  .brand .dot {
    width: 82px; height: 82px; border-radius: 50%;
    border: 7px solid var(--blue); margin-right: 20px;
  }
  .brand .wordmark {
    font-size: 36px; font-weight: 700; letter-spacing: 2px; color: var(--blue);
    text-transform: uppercase; line-height: 1;
  }

  .location {
    position: absolute; right: 48px; bottom: 46px; width: 260px; text-align: right;
    border-top: 1px solid var(--rule); padding-top: 14px;
  }
  .location .company {
    font-size: 16px; font-weight: 700; letter-spacing: 1px; color: var(--blue); text-transform: uppercase;
  }
  .location .city { font-size: 17px; color: var(--ink); }

  /* Back */
  .card--back {
    background: radial-gradient(ellipse at 35% 40%, var(--blue-light) 0%, var(--blue) 45%, var(--blue-deep) 100%);
    display: flex; flex-direction: column; align-items: center; justify-content: center; gap: 26px;
  }
  .card--back .wordmark {
    font-size: 58px; font-weight: 700; letter-spacing: 4px; color: var(--white);
    text-transform: uppercase; line-height: 1;
  }
  .card--back .url { font-size: 19px; color: var(--white); letter-spacing: .5px; }
</style>
</head>
<body>
<main class="stage">

  <section class="card card--front" aria-label="Business card, front">
    <div class="contact">
      <p class="name"><span class="first">Daniel</span> <span class="last">Carter</span></p>
      <p class="role">Managing Director</p>
      <div class="divider"></div>
      <ul>
        <li>
          <svg viewBox="0 0 16 16" aria-hidden="true"><rect x="3" y="1" width="10" height="14" rx="2" fill="none" stroke="var(--blue)" stroke-width="2"/><circle cx="8" cy="12" r="1" fill="var(--blue)"/></svg>
          044 555 0142
        </li>
        <li>
          <svg viewBox="0 0 16 16" aria-hidden="true"><rect x="1" y="3" width="14" height="10" fill="var(--blue)"/><path d="M1 3 L8 9 L15 3" fill="none" stroke="var(--white)" stroke-width="1.4"/></svg>
          ElenaVT@talkbridge-demo.co.uk
        </li>
        <li>
          <svg viewBox="0 0 16 16" aria-hidden="true"><circle cx="8" cy="8" r="7" fill="var(--blue)"/><path d="M1 8 H15 M8 1 C4 5 4 11 8 15 M8 1 C12 5 12 11 8 15" fill="none" stroke="var(--white)" stroke-width="1"/></svg>
          www.TalkBridge-demo.co.uk
        </li>
      </ul>
    </div>

    <div class="brand">
      <span class="dot" aria-hidden="true"></span>
      <span class="wordmark">TalkBridge</span>
    </div>

    <div class="location">
      <p class="company">TalkBridge</p>
      <p class="city">London, UK</p>
    </div>
    <div class="edge"></div>
  </section>

  <section class="card card--back" aria-label="Business card, back">
    <p class="wordmark">TalkBridge</p>
    <p class="url">www.TalkBridge-demo.co.uk</p>
  </section>

</main>
</body>
</html>
```